Business Card Upgrade

I have designed our business card using our new logo. I think it needs imporovements. We used to have two cards for our business. One card was for our software business, and the other was for our consulting business. We are now in the process of combining our websites, marketing, name, and a new logo.

Our goal is to have a really sharp professional logo. One reason I designed the card the way I did was that our Titles are sometimes long, and by separating the person's name and title, it shows up very well and the title can be adjusted no matter how long it is. Sometimes the title can be 4 or 5 words or more.

We really like our logo on black as it shows up very nice. Our PMS colors are as follows: 368C and 459C.

The Designer that will be working with us will need to deliver the following:

The front and back of the Business Card Design will need to be delivered in a high quality JPEG, and
The front and back of the Business Card Design in Illustrator Format .ai
Any fonts will need to be sent to us if they are not standard and are required to open the Illustrator file correctly.

To help us get a good idea of the card with a title, please use the title: " Director of Software Development "

NOTE: The chosen designer will be selected to design our new letterhead within 2 weeks from the closing of this contest.
Updates

To help us make sure the card design works with longer titles, please use the followign job title on the card:  

"Director of Software and Product Development"

 

ALL DESIGNERS:

1. I appreciate the different angles you are showing the cards, but please be sure and always show the direct view, so I can see the layout and what the person I hand the card will see.

2. Please do not use white.  Please use off white as I don't care for white cards and they get dirty easy and do not represent the designs well.

Dear Designers,

Please provide samples straight one as a viewer of the card will see.  Some of the angles that are presented make it impossible to tell how everything fits, and sometimes even makes areas look skewed. So, please provide a straight sample view.

Target Market(s)

Keystone 400 company executives such as Vice Presidents, and Directors

Industry/Entity Type

Software

Requirements
Must have
• Professional looking Card.

Our customers are Directors, Vice Presidents, and Presidents of companies as large as Keystone 400 companies. The card needs to get attention wile still looking professional.

Delivery of the finished product in Illustrator Format with any fonts needed to edit the text or open the file.

The card will be a heavy stock with a soft touch coating for that silk feel.

```html
<!DOCTYPE html>
<html lang="en">
<head>
<meta charset="utf-8">
<title>Portvale Trade Corporation – Business Card</title>
<link rel="stylesheet" href="https://fonts.googleapis.com/css2?family=Lato:wght@400;700&display=swap">
<style>
  :root {
    --backdrop: #d9d3c9;
    --card: #000000;
    --green: #4fa83d;
    --gold: #e4d49a;
    --card-shadow: rgba(0, 0, 0, 0.35);
  }
  * { margin: 0; padding: 0; box-sizing: border-box; }
  html, body {
    width: 1200px; height: 1000px; overflow: hidden;
    background: var(--backdrop);
    font-family: "Lato", Arial, sans-serif;
  }
  .canvas { position: relative; width: 1200px; height: 1000px; }
  .card {
    position: absolute; width: 693px; height: 395px;
    background: var(--card);
    box-shadow: 0 6px 18px var(--card-shadow);
  }
  .card--front { left: 102px; top: 72px; }
  .card--back { left: 401px; top: 526px; }

  /* front */
  .brand-name {
    position: absolute; color: var(--green); font-weight: 700;
    text-transform: uppercase; text-align: center; line-height: 1.15;
  }
  .card--front .brand-name {
    left: 40px; width: 290px; top: 58px; font-size: 26px; letter-spacing: 2px;
  }
  .card--front .brand-name small { display: block; font-size: 15px; letter-spacing: 3px; }
  .divider {
    position: absolute; left: 361px; top: 43px; width: 2px; height: 88px;
    background: var(--green);
  }
  .services {
    position: absolute; left: 380px; top: 68px; width: 280px;
    color: var(--gold); font-size: 13px; letter-spacing: 0.5px;
    text-align: center; line-height: 20px;
  }
  .services .sep { color: var(--green); margin: 0 3px; }
  .side-bar {
    position: absolute; top: 125px; width: 11px; height: 159px; background: var(--green);
  }
  .side-bar--left { left: 0; }
  .side-bar--right { right: 0; }
  .person { position: absolute; left: 69px; top: 187px; }
  .person-name {
    color: var(--green); font-size: 36px; font-weight: 400; letter-spacing: 0.5px; line-height: 1;
  }
  .person-title { color: var(--gold); font-size: 17px; margin-top: 2px; }
  .contact { position: absolute; left: 429px; top: 158px; list-style: none; }
  .contact li {
    display: flex; align-items: flex-start; color: var(--gold);
    font-size: 13px; line-height: 16px; margin-bottom: 9px;
  }
  .contact svg { width: 14px; height: 14px; margin-right: 8px; flex: none; fill: var(--green); }
  .tagline {
    position: absolute; left: 0; width: 100%; text-align: center;
    font-size: 14px; letter-spacing: 1px; text-transform: uppercase;
  }
  .card--front .tagline { top: 361px; color: var(--green); }
  .card--front .tagline em { color: var(--gold); font-style: normal; }

  /* back */
  .card--back .tagline { top: 35px; color: var(--gold); }
  .card--back .tagline em { color: var(--green); font-style: normal; }
  .card--back .brand-name {
    left: 0; width: 100%; top: 122px; font-size: 62px; letter-spacing: 6px;
  }
  .card--back .brand-name small { display: block; font-size: 30px; letter-spacing: 10px; margin-top: 6px; }
  .website {
    position: absolute; left: 0; width: 100%; top: 355px; text-align: center;
    color: var(--gold); font-size: 13px; font-weight: 700;
  }
  .website span { color: var(--green); }
</style>
</head>
<body>
<main class="canvas">

  <section class="card card--front" aria-label="Business card front">
    <div class="brand-name">Portvale<small>Trade Corporation</small></div>
    <div class="divider"></div>
    <p class="services">
      Consulting<span class="sep">|</span>Compliance Software<br>
      Operations<span class="sep">|</span>Administration
    </p>
    <div class="side-bar side-bar--left"></div>
    <div class="side-bar side-bar--right"></div>

    <div class="person">
      <h1 class="person-name">DALE FENWICK</h1>
      <p class="person-title">Director of Software Development</p>
    </div>

    <ul class="contact">
      <li>
        <svg viewBox="0 0 24 24"><path d="M6.6 10.8a15 15 0 0 0 6.6 6.6l2.2-2.2c.3-.3.7-.4 1-.2 1.1.4 2.3.6 3.6.6.6 0 1 .4 1 1V20c0 .6-.4 1-1 1A17 17 0 0 1 3 4c0-.6.4-1 1-1h3.5c.6 0 1 .4 1 1 0 1.3.2 2.5.6 3.6.1.3 0 .7-.2 1z"/></svg>
        + 251.555.0148
      </li>
      <li>
        <svg viewBox="0 0 24 24"><path d="M2 5h20v14H2z M4 7v.5l8 5 8-5V7l-8 5z" fill-rule="evenodd"/></svg>
        dfenwick@portvalecorp.com
      </li>
      <li>
        <svg viewBox="0 0 24 24"><path d="M12 2a10 10 0 1 0 0 20 10 10 0 0 0 0-20zm6.9 6h-3a15 15 0 0 0-1.3-3.9A8 8 0 0 1 18.9 8zM12 4c.8 1.2 1.5 2.5 1.9 4h-3.8c.4-1.5 1.1-2.8 1.9-4zM4.3 14a8 8 0 0 1 0-4h3.4a16 16 0 0 0 0 4zm.8 2h3a15 15 0 0 0 1.3 3.9A8 8 0 0 1 5.1 16zm3-8h-3a8 8 0 0 1 4.3-3.9C8.8 5.3 8.4 6.6 8.1 8zM12 20c-.8-1.2-1.5-2.5-1.9-4h3.8c-.4 1.5-1.1 2.8-1.9 4zm2.3-6H9.7a14 14 0 0 1 0-4h4.6a14 14 0 0 1 0 4zm.3 5.9c.6-1.2 1-2.5 1.3-3.9h3a8 8 0 0 1-4.3 3.9zm1.7-5.9a16 16 0 0 0 0-4h3.4a8 8 0 0 1 0 4z"/></svg>
        portvalecorp.com
      </li>
      <li>
        <svg viewBox="0 0 24 24"><path d="M12 2a7 7 0 0 0-7 7c0 5.2 7 13 7 13s7-7.8 7-13a7 7 0 0 0-7-7zm0 9.5a2.5 2.5 0 1 1 0-5 2.5 2.5 0 0 1 0 5z"/></svg>
        <span>1480 Harbor Mill Road<br>Tidewater, AL 36600</span>
      </li>
    </ul>

    <p class="tagline">The only frim with enough expertise to offer every <em>FTZ</em> solutions</p>
  </section>

  <section class="card card--back" aria-label="Business card back">
    <p class="tagline">The only frim with enough expertise to offer every <em>FTZ</em> solutions</p>
    <div class="brand-name">Portvale<small>Trade Corporation</small></div>
    <p class="website">WWW.<span>PORTVALECORP</span>.COM</p>
  </section>

</main>
</body>
</html>
```